"Beyond Marrow Cay" Fictional Book Cover

BEYOND MARROW CAY
By: Dale Pruitt

Here's the intro .

"It had been nearly forty years since Ted Larraby last went to the island from where he was raised. Three months earlier he never would have thought about ever coming back. But life is weird. Things happen quickly and plans change, especially when your very life is at stake. The reason he was going back wasn’t to see old friends...no, no, no. They’re all dead. Of all the kids he grew up with on the island who moved off, he’s the only one still alive. Why?"

Pretty much all just a Lumeno book, by the way.

Target Market(s)

fiction readers

Requirements
Must have
• Somewhat of a dark, mysterious cover is what I'd like to see. Use your imagination. I've never written a fiction book before so I'm very open to ideas

Needs to have my name, DALE PRUITT at the bottom. like my other books, all of which are non-fiction
Nice to have
• Mysterious is what I'm looking for. NOT A HORROR story though. More a guy who left the island years ago, but is being called back to escape the rat race of modern, consumerist culture.

Please remember this NEEDS to jump out as a thumbnail on Bookvale as people are browsing. Mainly the WORDS need to stick out. Lighter words on a say a blue background.

If you want to try to use the attached pic, or something like this, to reflect an island in the cover, that'd be good.

I've also uploaded a couple images I purchased from Pixelcrate, hopefully you can make something work with these.

```html
<!DOCTYPE html>
<html lang="en">
<head>
<meta charset="utf-8">
<title>Beyond Marrow Cay — Book Cover</title>
<link rel="stylesheet" href="https://fonts.googleapis.com/css2?family=Alfa+Slab+One&family=Montserrat:wght@800&display=swap">
<style>
  :root {
    --page: #ffffff;
    --sky-top: #2c2a5c;
    --sky-mid: #5c3f6e;
    --dusk: #9a6077;
    --glow: #c98a6e;
    --shore: #0c0618;
    --frame: #b79ce0;
    --title: #ffffff;
    --title-edge: #3a1f6b;
    --title-glow: #b43cff;
    --author: #ffffff;
    --author-edge: #2a7bff;
  }
  * { margin: 0; padding: 0; box-sizing: border-box; }
  html, body { width: 950px; height: 1200px; overflow: hidden; background: var(--page); }
  .canvas { position: relative; width: 950px; height: 1200px; background: var(--page); }
  .cover {
    position: absolute; left: 121px; top: 134px; width: 713px; height: 884px; overflow: hidden;
  }
  .cover-scene {
    position: absolute; inset: 0;
    background:
      radial-gradient(ellipse 60% 30% at 12% 58%, rgba(201,138,110,.85), rgba(201,138,110,0) 70%),
      radial-gradient(ellipse 45% 55% at 92% 50%, rgba(20,28,20,.9), rgba(20,28,20,0) 70%),
      linear-gradient(180deg, var(--sky-top) 0%, var(--sky-mid) 22%, var(--dusk) 45%, #3b2240 62%, var(--shore) 78%, var(--shore) 100%);
  }
  .title-frame {
    position: absolute; left: 72px; top: 85px; width: 574px; height: 563px;
    border: 2px solid var(--frame);
    box-shadow: 0 0 14px rgba(183,156,224,.7), inset 0 0 14px rgba(183,156,224,.35);
    background: rgba(40,20,60,.12);
  }
  .book-title {
    position: absolute; left: 0; right: 0; top: 170px;
    font-family: "Alfa Slab One", serif; color: var(--title);
    text-align: center; line-height: 1; letter-spacing: 1px;
  }
  .book-title span {
    display: block;
    text-shadow:
      1px 1px 0 var(--title-edge), 2px 2px 0 var(--title-edge),
      3px 3px 0 var(--title-edge), 4px 4px 0 var(--title-edge),
      5px 5px 0 #1a0e33,
      0 0 18px rgba(180,60,255,.8), 0 0 36px rgba(180,60,255,.5);
  }
  .title-line-1 { font-size: 86px; margin-bottom: 44px; }
  .title-line-2 { font-size: 78px; margin-bottom: 44px; }
  .title-line-3 { font-size: 96px; }
  .author-name {
    position: absolute; left: 0; right: 0; top: 730px;
    font-family: "Montserrat", sans-serif; font-weight: 800; font-size: 54px;
    color: var(--author); text-align: center; letter-spacing: 1px;
    text-shadow: -2px 1px 0 var(--author-edge), 0 0 10px rgba(150,120,255,.5);
  }
</style>
</head>
<body>
  <main class="canvas">
    <section class="cover">
      <div class="cover-scene" role="img" aria-label="Dusk photograph of a wooded island shoreline with a lighthouse house among trees, purple sky with lightning streaks over dark water"></div>
      <div class="title-frame"></div>
      <h1 class="book-title">
        <span class="title-line-1">BEYOND</span>
        <span class="title-line-2">MARROW</span>
        <span class="title-line-3">CAY</span>
      </h1>
      <p class="author-name">DALE PRUITT</p>
    </section>
  </main>
</body>
</html>
```